Brightwell is a company offering Colon Hydrotherapy (or colonics)

Brightwell offers Colon Hydrotherapy using an innovative FDA approved system from the USA. The system is called the TORVA system. The clinic is based in Whangarei, Northland and is the first business of this kind for Northland.
I used to use a design from the Printlane website - a water symbol. However, I want a design that will convey freshness. I want something new and clean which conveys vitality and revitalisation .... perhaps water or bubbles but which brings across the idea of detoxing (which is what colon hydrotherapy does)
The clinic will only be completed in April so for now I have put my mobile number but once in the clinic this will need to be changed to a landline number ... the email address will also change. Thanks for any ideas you give me,
Updates

Hi. I need the name Brightwell first and foremost as this is the name of the Company Underneath this it has to say Colon Hydrotherapy to let people know what Brightwell is My name underneath that would be Miriam Holloway And all contact details to follow this. Thanks !

Target Market(s)

People who are wanting to "detox" and focusing on their health and wellbeing

Industry/Entity Type

Clinic

Contact Information for Business Card

Brightwell
Colon Hydrotherapy
Miriam Holloway
Unit B, 42c Harbour Lane, Whangarei

021 0487 3926
brightwellcare@mailnest.example

Font styles to use
Serif

Colors
cee9f6
33a6d7
86cae6

Requirements
Must have
• Stand out with colour or logo

```html
<!DOCTYPE html>
<html lang="en">
<head>
<meta charset="utf-8">
<title>Brightwell Colon Hydrotherapy – Business Card</title>
<link href="https://fonts.googleapis.com/css2?family=Questrial&family=Open+Sans:wght@400;600;700&display=swap" rel="stylesheet">
<style>
  :root {
    --ink-blue: #1f7fc4;
    --deep-blue: #1a86cc;
    --mid-blue: #33a6d7;
    --soft-blue: #86cae6;
    --pale-blue: #cee9f6;
    --white: #ffffff;
    --backdrop: #eef1f4;
  }
  html, body {
    margin: 0;
    width: 1200px;
    height: 1000px;
    overflow: hidden;
    background: var(--backdrop);
  }
  .canvas {
    position: relative;
    width: 1200px;
    height: 1000px;
  }
  .card {
    position: absolute;
    left: 265px;
    width: 665px;
    height: 397px;
    border-radius: 22px;
    overflow: hidden;
    box-shadow: 0 4px 14px rgba(0,0,0,0.18);
  }
  .card--front { top: 73px; background: var(--white); }
  .card--back {
    top: 533px;
    background: radial-gradient(ellipse 60% 65% at 45% 45%, var(--soft-blue) 0%, var(--mid-blue) 55%, var(--deep-blue) 100%);
  }
  .card__wave { position: absolute; inset: 0; }

  .brand { position: absolute; font-family: "Questrial", sans-serif; }
  .brand__row { display: flex; align-items: center; }
  .brand__dot { border-radius: 50%; flex: none; }
  .brand__name { line-height: 1; font-weight: 400; }
  .brand__tagline { line-height: 1; }

  .card--front .brand { left: 40px; top: 100px; color: var(--ink-blue); }
  .card--front .brand__dot { width: 26px; height: 26px; background: var(--mid-blue); margin-right: 14px; }
  .card--front .brand__name { font-size: 54px; }
  .card--front .brand__tagline { font-size: 23px; margin: 8px 0 0 40px; color: var(--mid-blue); }

  .holder-name {
    position: absolute; right: 32px; top: 124px; margin: 0;
    font-family: "Open Sans", sans-serif; font-weight: 700; font-size: 22px;
    color: var(--ink-blue);
  }
  .address {
    position: absolute; left: 33px; top: 300px; margin: 0;
    font-family: "Open Sans", sans-serif; color: var(--white);
    font-style: normal; font-size: 15px; line-height: 22px;
  }
  .address__title { font-weight: 700; font-size: 16px; display: block; margin-bottom: 2px; }
  .contact {
    position: absolute; right: 32px; top: 268px; margin: 0; text-align: right;
    font-family: "Open Sans", sans-serif; color: var(--white); line-height: 24px;
  }
  .contact__phone { font-weight: 700; font-size: 17px; display: block; }
  .contact__email { font-size: 17px; display: block; }

  .card--back .brand { left: 0; right: 0; top: 140px; display: flex; flex-direction: column; align-items: center; color: var(--white); }
  .card--back .brand__dot { width: 40px; height: 40px; background: var(--white); margin-right: 20px; }
  .card--back .brand__name { font-size: 78px; }
  .card--back .brand__tagline { font-size: 33px; margin: 12px 0 0 60px; }
</style>
</head>
<body>
<main class="canvas">
  <section class="card card--front" aria-label="Business card front">
    <svg class="card__wave" viewBox="0 0 665 397" width="665" height="397" aria-hidden="true">
      <defs>
        <radialGradient id="frontBlue" cx="0.55" cy="0.35" r="0.7">
          <stop offset="0" stop-color="#86cae6"/>
          <stop offset="0.6" stop-color="#33a6d7"/>
          <stop offset="1" stop-color="#1a86cc"/>
        </radialGradient>
      </defs>
      <path d="M0,238 C160,290 300,285 430,230 C530,190 610,182 665,186 L665,205 C600,200 520,215 430,248 C300,295 150,300 0,262 Z" fill="#86cae6"/>
      <path d="M0,262 C150,300 300,295 430,248 C520,215 600,200 665,205 L665,397 L0,397 Z" fill="url(#frontBlue)"/>
      <path d="M300,283 C360,275 400,258 440,242 C530,208 600,196 665,198" fill="none" stroke="#ffffff" stroke-width="2"/>
    </svg>

    <div class="brand">
      <div class="brand__row"><span class="brand__dot"></span><span class="brand__name">Brightwell</span></div>
      <div class="brand__tagline">Colon Hydrotherapy</div>
    </div>

    <p class="holder-name">Miriam Holloway</p>

    <address class="address">
      <span class="address__title">Brightwell Colon Hydrotherapy</span>
      Unit B, 42c Harbour Lane,<br>Whangarei
    </address>

    <p class="contact">
      <span class="contact__phone">021 0487 3926</span>
      <span class="contact__email">brightwellcare@mailnest.example</span>
    </p>
  </section>

  <section class="card card--back" aria-label="Business card back">
    <div class="brand">
      <div class="brand__row"><span class="brand__dot"></span><span class="brand__name">Brightwell</span></div>
      <div class="brand__tagline">Colon Hydrotherapy</div>
    </div>
  </section>
</main>
</body>
</html>
```